Business Card for Restaurant Vendal

This project consist of creating 2 design for business card of restaurant named Vendal.

The attached specs below are 'ONLY SUGGESTION' if you have others ideas. You are welcome to post it.

1) Restaurant Card

Adresse:
2784 Côte du Pinard Vert
Montréal (Qc) H4K 3T8

Website:
www.ven-dal.ca

Phone:
438-719-2046

2) Employee Card

Name: Lorna Pik
Title: Owner

Address:
2784 Côte du Pinard Vert
Montréal (Qc) H4K 3T8

Email:lorna@ven-dal.ca
Phone Number:438-719-2046
Cellphone Number:514-830-4162

 The attached specs are 'ONLY SUGGESTION' if you have others ideas.  You are welcome to post it.

Industry/Entity Type

Restaurant

Requirements
Must have
• UV Card Spot

To print Spot UV business cards you would have to submit 2 files for each side. The first file "base" would be your regular design file as it would have been in any other case. The 2nd file "UV mask" is a black/white file. The BLACK color will indicate the areas that will be covered with the UV high gloss finish. To upload the files, please combine front design and front mask file in one P
Nice to have
• 1) The font of the logo should be ink effect
2) black background with wallpaper effect
3) The specs below are 'ONLY SUGGESTION' if you have others ideas. You are welcome to post it.

```html
<!DOCTYPE html>
<html lang="fr">
<head>
<meta charset="utf-8">
<title>Restaurant Vendal — Business Cards</title>
<link rel="stylesheet" href="https://fonts.googleapis.com/css2?family=Cinzel:wght@400;600&family=Noto+Serif+JP:wght@600&display=swap">
<style>
  :root {
    --backdrop: #2b2623;
    --card: #1d1c1d;
    --card-edge: #262426;
    --logo-grey: #8d8b8d;
    --tag-grey: #6f6d70;
    --kanji-grey: #4a484b;
    --accent-red: #a8251c;
    --icon-grey: #8a888a;
    --lantern-dark: #151415;
    --lantern-mid: #2e2c2e;
  }
  * { margin: 0; padding: 0; box-sizing: border-box; }
  html, body { width: 1200px; height: 900px; overflow: hidden; }
  body {
    background: var(--backdrop);
    font-family: "Cinzel", "Times New Roman", serif;
    position: relative;
  }
  .card {
    position: absolute;
    left: 260px;
    width: 680px;
    height: 389px;
    border-radius: 22px;
    background: linear-gradient(160deg, var(--card-edge), var(--card) 55%, #181718);
    box-shadow: 0 14px 30px rgba(0,0,0,.45);
    overflow: hidden;
  }
  .card--front { top: 40px; }
  .card--back { top: 470px; }

  .lantern {
    position: absolute;
    border-radius: 46% 46% 42% 42%;
    background: radial-gradient(circle at 45% 40%, var(--lantern-mid), var(--lantern-dark) 75%);
  }
  .card--front .lantern { left: 100px; top: 130px; width: 140px; height: 132px; }
  .card--back .lantern { left: 430px; top: 40px; width: 140px; height: 132px; }

  .divider {
    position: absolute;
    left: 280px; top: 120px;
    width: 2px; height: 150px;
    background: linear-gradient(var(--card), #0f0e0f, var(--card));
  }

  .brand {
    position: absolute;
    display: flex;
    flex-direction: column;
    align-items: flex-start;
  }
  .brand__row { display: flex; align-items: flex-start; gap: 10px; }
  .brand__name {
    font-family: "Cinzel", "Times New Roman", serif;
    font-weight: 600;
    color: var(--logo-grey);
    line-height: 1;
    white-space: nowrap;
  }
  .brand__dot { flex: none; border-radius: 50%; background: var(--accent-red); }
  .brand__tag {
    font-family: "Cinzel", "Times New Roman", serif;
    color: var(--tag-grey);
    letter-spacing: .5px;
    white-space: nowrap;
  }
  .card--front .brand { left: 318px; top: 145px; }
  .card--front .brand__name { font-size: 56px; }
  .card--front .brand__dot { width: 26px; height: 26px; }
  .card--front .brand__tag { font-size: 14px; margin-top: 12px; }

  .card--back .brand { left: 420px; top: 190px; }
  .card--back .brand__name { font-size: 40px; color: #3f3d40; }
  .card--back .brand__dot { width: 18px; height: 18px; }
  .card--back .brand__tag { font-size: 10px; margin-top: 6px; color: #3b393c; }

  .kanji {
    position: absolute;
    left: 100px; top: 80px;
    font-family: "Noto Serif JP", serif;
    font-weight: 600;
    font-size: 56px;
    letter-spacing: 8px;
    color: var(--kanji-grey);
  }
  .contact {
    position: absolute;
    display: flex;
    gap: 14px;
    color: var(--accent-red);
    font-size: 19px;
    line-height: 1.2;
  }
  .contact svg { flex: none; margin-top: 3px; }
  .contact--address { left: 100px; top: 228px; }
  .contact--phone { left: 100px; top: 306px; font-size: 24px; }
  .website {
    position: absolute;
    left: 468px; top: 300px;
    color: var(--accent-red);
    font-size: 16px;
    letter-spacing: .5px;
  }
</style>
</head>
<body>
  <section class="card card--front" aria-label="Card front">
    <div class="lantern" role="img" aria-label="Glossy black paper lantern illustration"></div>
    <div class="divider"></div>
    <div class="brand">
      <div class="brand__row">
        <span class="brand__name">Vendal</span>
        <span class="brand__dot"></span>
      </div>
      <span class="brand__tag">Resto-Bar Japonais · Izakaya · 居酒屋</span>
    </div>
  </section>

  <section class="card card--back" aria-label="Card back">
    <div class="kanji">居酒屋</div>
    <div class="contact contact--address">
      <svg width="14" height="18" viewBox="0 0 14 18" aria-hidden="true">
        <path d="M7 0a7 7 0 0 0-7 7c0 5 7 11 7 11s7-6 7-11a7 7 0 0 0-7-7z" fill="var(--icon-grey)"/>
        <circle cx="7" cy="7" r="2.6" fill="var(--card)"/>
      </svg>
      <p>2784 Côte du Pinard Vert<br>Montréal (Qc) H4K 3T8</p>
    </div>
    <div class="contact contact--phone">
      <svg width="16" height="16" viewBox="0 0 16 16" aria-hidden="true">
        <circle cx="8" cy="8" r="7" fill="none" stroke="var(--icon-grey)" stroke-width="1.4"/>
        <path d="M5.5 4.5l1.5 1.5-1 1c.6 1.2 1.5 2.1 2.7 2.7l1-1 1.5 1.5-1.2 1.2c-2.5-.6-4.6-2.7-5.2-5.2z" fill="var(--icon-grey)"/>
      </svg>
      <p>438-719-2046</p>
    </div>
    <div class="lantern" role="img" aria-label="Glossy black paper lantern illustration"></div>
    <div class="brand">
      <div class="brand__row">
        <span class="brand__name">Vendal</span>
        <span class="brand__dot"></span>
      </div>
      <span class="brand__tag">Resto-Bar Japonais · Izakaya · 居酒屋</span>
    </div>
    <p class="website">www.ven-dal.ca</p>
  </section>
</body>
</html>
```